Gift Card/voucher Design for Beauty Clinic

I need a design for a gift card I Can use in all seasons for my Aesthetic clinic. The Logo is attached. The main colors we use are white and black, we are open for new suggestions to make an friendly yet professional impression. Ideally the gift card/voucher would be foldable.
The inside should contain the following fields:

Für:

Von:

Wert

Gültigkeit

```html
<!DOCTYPE html>
<html lang="de">
<head>
<meta charset="utf-8">
<title>Gutschein – Lena Hartmann</title>
<link href="https://fonts.googleapis.com/css2?family=Open+Sans:wght@700&family=Arimo:wght@400&family=Playfair+Display:wght@500&family=Mrs+Saint+Delafield&display=swap" rel="stylesheet">
<style>
  :root {
    --backdrop: #eeeeee;
    --card: #ffffff;
    --card-border: #b9b9b9;
    --ink: #1c2b36;
    --rule: #8a8f93;
  }
  html, body {
    margin: 0;
    padding: 0;
    width: 1200px;
    height: 1200px;
    overflow: hidden;
    background: var(--backdrop);
  }
  .voucher {
    position: absolute;
    left: 127px;
    top: 302px;
    width: 946px;
    height: 596px;
    box-sizing: border-box;
    background: var(--card);
    border: 1.5px solid var(--card-border);
    color: var(--ink);
  }
  .brand-mark {
    position: absolute;
    left: 70px;
    top: 68px;
    width: 165px;
    text-align: center;
    font-family: "Playfair Display", Georgia, serif;
    font-weight: 500;
    font-size: 15px;
    letter-spacing: 1.5px;
    line-height: 1.3;
    color: var(--ink);
  }
  .headline {
    position: absolute;
    left: 318px;
    top: 30px;
    width: 330px;
    height: 220px;
  }
  .headline-main {
    position: absolute;
    left: 0;
    top: 0;
    margin: 0;
    font-family: "Open Sans", Arial, sans-serif;
    font-weight: 700;
    font-size: 97px;
    line-height: 1;
    letter-spacing: -2px;
    color: var(--ink);
  }
  .headline-script {
    position: absolute;
    left: 4px;
    top: 40px;
    font-family: "Mrs Saint Delafield", cursive;
    font-size: 150px;
    line-height: 1;
    color: var(--ink);
    white-space: nowrap;
  }
  .field {
    position: absolute;
    left: 165px;
    right: 130px;
    display: flex;
    align-items: flex-end;
    font-family: "Arimo", Arial, sans-serif;
    font-size: 28px;
    line-height: 1;
    color: var(--ink);
  }
  .field-label { white-space: nowrap; }
  .field-line {
    flex: 1;
    border-bottom: 1.5px solid var(--rule);
    margin-left: 16px;
    margin-bottom: 4px;
  }
  .field--to { top: 254px; }
  .field--from { top: 311px; }
  .field--value { top: 369px; }
  .field--validity { top: 429px; }
  .field--validity .field-line { margin-left: 140px; }
  .signature {
    position: absolute;
    left: 0;
    right: 0;
    top: 544px;
    text-align: center;
    font-family: "Playfair Display", Georgia, serif;
    font-weight: 500;
    font-size: 23px;
    letter-spacing: 2.5px;
    color: var(--ink);
  }
</style>
</head>
<body>
  <main class="voucher">
    <div class="brand-mark">LENA<br>HARTMANN</div>

    <div class="headline">
      <h1 class="headline-main">A GIFT</h1>
      <span class="headline-script">for you</span>
    </div>

    <div class="field field--to"><span class="field-label">FÜR:</span><span class="field-line"></span></div>
    <div class="field field--from"><span class="field-label">VON:</span><span class="field-line"></span></div>
    <div class="field field--value"><span class="field-label">WERT</span><span class="field-line"></span></div>
    <div class="field field--validity"><span class="field-label">GÜLTIGKEIT</span><span class="field-line"></span></div>

    <div class="signature">LENA HARTMANN</div>
  </main>
</body>
</html>
```